A gateway to the eyes of potential Telmar Candidates and Clients

We are looking for a brochure that will grab attention, all most along the lines of an infogram. The business supplies people to the construction sector. So we want it simple but sharp.

I would like the brochure to be able to have a half fold effect when printed but the main focus will be to use it in an e-brochure format.

Main pages will be as follows:

About Us: Which will have a bit about the management team and some pictures.

Services: information for both candidate and clients.

Why us?:

Contact: Location, contact numbers etc.

FOR CONTENTS:
website will give you the content required. www.telmarconstruction.co.uk

Project Deadline Extended Reason: Project was moved from a flyer to a brochure and the logo didn't upload. So I will be uploading my new logo and it will give additional time to get designs in. Cheers Added Monday, June 20, 2016

Target Market(s)

Clients and candidates for the construction market

Industry/Entity Type

Business

Requirements
Must have
• Bold and strong images of the construction sector. A simple to read format. Also needs to look good in an electronic format.
Nice to have
• I like the idea of a black and white model but with certain parts of the images highlighted in our colours.
Should not have
• Too much of a complex lay out.

```html
<!DOCTYPE html>
<html lang="en">
<head>
<meta charset="utf-8">
<title>Telmar Construction – Folder Spread</title>
<link href="https://fonts.googleapis.com/css2?family=Lato:wght@400;700&display=swap" rel="stylesheet">
<style>
  :root {
    --orange: #ef8422;
    --orange-deep: #e27819;
    --blue: #1d4aa0;
    --navy: #1f3f8f;
    --white: #ffffff;
    --ink: #333333;
    --stage: #e9e9eb;
    --fold-grey: #9a9a9a;
  }
  * { box-sizing: border-box; margin: 0; padding: 0; }
  html, body {
    width: 1200px; height: 794px; overflow: hidden;
    background: var(--stage);
    font-family: "Lato", Arial, sans-serif;
  }
  .spread {
    position: absolute; left: 70px; top: 37px;
    width: 1060px; height: 720px;
    display: flex;
    box-shadow: 0 10px 30px rgba(0,0,0,.18);
  }
  .panel { position: relative; width: 530px; height: 720px; overflow: hidden; background: var(--white); }

  /* back panel */
  .back-art { position: absolute; inset: 0; }
  .back-footer {
    position: absolute; left: 0; right: 0; bottom: 0; height: 150px;
    display: flex; align-items: center; gap: 34px; padding-left: 52px;
  }
  .brand { display: flex; align-items: center; gap: 10px; }
  .brand-mark { width: 22px; height: 22px; background: var(--orange); }
  .brand-name { font-weight: 700; font-size: 30px; color: var(--orange); letter-spacing: 1px; }
  .address { font-family: Arial, Helvetica, sans-serif; font-size: 11.5px; line-height: 16px; color: var(--ink); }
  .address .web { color: var(--orange); font-weight: 700; }

  /* front panel */
  .front { background: linear-gradient(90deg, var(--fold-grey) 0%, #d6d6d6 22%, var(--white) 48%); }
  .front .brand { position: absolute; top: 58px; left: 0; right: 0; justify-content: center; }
  .front .brand-name { font-size: 34px; }
  .photo { position: absolute; left: 0; top: 0; }
  .tagline {
    position: absolute; left: 0; right: 0; top: 572px; text-align: center;
    font-size: 24px; line-height: 30px;
  }
  .tagline .lead { color: var(--orange); font-weight: 700; display: block; }
  .tagline .rest { color: var(--blue); }
</style>
</head>
<body>
<main class="spread">
  <section class="panel back">
    <svg class="back-art" width="530" height="720" viewBox="0 0 530 720">
      <path d="M0 0 H530 V515 Q260 585 0 610 Z" fill="var(--orange)"/>
      <path d="M0 610 Q260 585 530 515" fill="none" stroke="var(--blue)" stroke-width="7"/>
    </svg>
    <div class="back-footer">
      <div class="brand">
        <span class="brand-mark"></span>
        <span class="brand-name">TELMAR</span>
      </div>
      <address class="address">
        Hollin Corner, Marsh Lane Rd<br>
        West Sussex&nbsp; RH12 4QT<br>
        Tel: 01293 640318<br>
        info@telmarconstruction.co.uk<br>
        <span class="web">www.telmarconstruction.co.uk</span>
      </address>
    </div>
  </section>

  <section class="panel front">
    <div class="brand">
      <span class="brand-mark"></span>
      <span class="brand-name">TELMAR</span>
    </div>
    <svg class="photo" width="530" height="720" viewBox="0 0 530 720" role="img"
         aria-label="Photograph of two construction professionals in hard hats, one holding rolled plans">
      <defs>
        <linearGradient id="photoTone" x1="0" y1="0" x2="1" y2="1">
          <stop offset="0" stop-color="#6b7c98"/>
          <stop offset="0.5" stop-color="#2e3442"/>
          <stop offset="1" stop-color="#b9c4c0"/>
        </linearGradient>
      </defs>
      <polygon points="90,250 200,160 300,185 410,200 470,390 330,540 230,500 150,470"
               fill="url(#photoTone)"/>
    </svg>
    <p class="tagline">
      <span class="lead">Telmar Construction</span>
      <span class="rest">is in your corner.</span>
    </p>
  </section>
</main>
</body>
</html>
```